Flyer für ambulanten Pflegedienst
Zielgruppe
Ambulanter Pflegedienst, Potentielle Kunden für Grund- und Behandlungspflege, nicht nur Pflegebedürftige, sondern auch Angehörige. Flyer dient zur Auslage, beispielsweise in Wartezimmern von Ärzten.
Aufgabenstellung
Ausführliches Briefing mit Aufbau und Text in der Anlage, ebenso das Bildmaterial, Fonts, Logos. Flyer in A4 Wickelfalz, bitte die Gestaltungsvorlage mit den Maßen des Druckanbieters (ebenfalls anbei) beachten. Vorerst hauptsächlich KI-generierte/Stockfotos vorhanden, Fotoshooting folgt im Juli und Bilder werden dann ggf. nochmal ersetzt um persönliche Ebene zu erzeugen. Der erste Wurf muss aber vorerst so erfolgen. Übergabe der Daten: Druckfähiges PDF, PDF mit Ebenen und AI

```html
<!DOCTYPE html>
<html lang="de">
<head>
<meta charset="utf-8">
<title>Flyer Ambulanter Pflegedienst</title>
<link rel="stylesheet" href="https://fonts.googleapis.com/css2?family=Outfit:wght@300;400;500;600;700&family=Libre+Caslon+Text:wght@400&display=swap">
<style>
:root{
  --blue:#123f96;
  --navy:#243f80;
  --light:#c3d7f1;
  --lighter:#e3edf9;
  --green:#2b9a4f;
  --ink:#111;
  --grey:#555;
  --rule:#b4c6df;
  --sans:'Outfit',sans-serif;
  --serif:'Libre Caslon Text',serif;
}
*{margin:0;padding:0;box-sizing:border-box}
html,body{width:891px;height:1200px;overflow:hidden;background:#fff}
body{position:relative;font-family:var(--sans);color:var(--ink)}
.panel{position:absolute;width:275px;height:578px;overflow:hidden;background:#fff;outline:1px solid #ddd}
.p1{left:18px;top:16px}.p2{left:308px;top:16px}.p3{left:598px;top:16px}
.p4{left:17px;top:609px}.p5{left:308px;top:609px}.p6{left:599px;top:609px}
.abs{position:absolute}
.svgfill{position:absolute;left:0;top:0;width:275px;height:578px}
.serif{font-family:var(--serif);font-weight:400}
.blue{color:var(--blue)}
.kicker{font-size:15px;color:var(--blue);font-weight:400}
.headline{font-weight:600;line-height:1;letter-spacing:-.3px}
.headline .serif{letter-spacing:-.5px}
.body{font-size:9.2px;font-weight:300;line-height:1.55;color:#333}
.photo{position:absolute}
.badge{position:absolute;border-radius:50%;background:#eef2f8;display:flex;align-items:center;justify-content:center;text-align:center;font-family:var(--sans);font-weight:500;color:var(--blue);line-height:1.1}
/* service list */
.services{position:absolute;left:22px;right:20px}
.service{display:flex;align-items:flex-start;gap:14px;border-top:1px solid var(--rule);padding:12px 0 12px 6px}
.service:last-child{border-bottom:1px solid var(--rule)}
.icon{flex:none;width:33px;height:33px;border-radius:50%;background:#fff;display:flex;align-items:center;justify-content:center}
.icon svg{width:18px;height:18px;fill:none;stroke:var(--blue);stroke-width:1.3}
.service h3{font-size:10px;font-weight:400;margin-top:2px}
.service p{font-size:5.2px;font-weight:300;line-height:1.55;color:#333;margin-top:3px}
/* quote */
.quote{position:absolute;color:var(--blue);font-weight:500;font-size:13.4px;line-height:1.15}
.quote-frame{position:absolute}
/* contact */
.contact{font-size:6.8px;font-weight:300;line-height:1.45;color:#222}
.contact .row{display:flex;gap:5px;align-items:center}
.contact svg{width:7px;height:7px;fill:none;stroke:currentColor;stroke-width:1.2;flex:none}
.dotted{position:absolute;left:26px;right:34px;border-top:1px dotted #aaa}
</style>
</head>
<body>

<!-- Panel 1: Titel -->
<section class="panel p1">
  <div class="photo" role="img" aria-label="Foto: Pflegekraft im Gespräch mit einer älteren Dame auf dem Sofa" style="left:0;top:0;width:275px;height:300px;background:linear-gradient(135deg,#6f7d6a 0%,#a7a99a 35%,#cfc3ad 60%,#3f7f72 100%)"></div>
  <svg class="svgfill" viewBox="0 0 275 578" aria-hidden="true">
    <path d="M0 280 C90 320 200 310 275 195 L275 260 C210 320 120 300 0 296 Z" fill="#fff"/>
    <path d="M0 276 C90 312 190 302 275 190 L275 245 C200 300 110 305 0 300 Z" fill="#123f96"/>
    <path d="M0 300 C110 305 200 300 275 245 L275 578 L0 578 Z" fill="#fff"/>
  </svg>
  <div class="badge" style="left:117px;top:210px;width:118px;height:92px;font-size:12px">Lindner<br>Hauspflege</div>
  <h1 class="headline abs" style="left:26px;top:323px;font-size:26px;line-height:1">
    <span class="serif">Weil das <span class="blue">eigene</span></span><br>Zuhause<br><span class="blue">Lebensqualität ist.</span>
  </h1>
  <div class="abs" style="left:14px;top:420px;width:261px;height:53px;background:var(--navy);color:#fff;font-size:15px;font-weight:500;line-height:1.15;padding:9px 12px">Ihr ambulanter<br>Pflegedienst für die Region.</div>
  <ul class="abs" style="left:26px;top:493px;list-style:none;font-size:11.5px;line-height:1.4">
    <li>o&nbsp;24h erreichbar</li>
    <li>o&nbsp;Persönliche Beratung</li>
    <li>o&nbsp;MD-geprüfte Qualität</li>
  </ul>
</section>

<!-- Panel 2: Wer wir sind -->
<section class="panel p2">
  <svg class="svgfill" viewBox="0 0 275 578" aria-hidden="true">
    <path d="M0 68 C80 35 180 18 275 20 L275 43 C180 40 90 48 0 68 Z" fill="#123f96"/>
    <path d="M0 578 L0 530 C110 520 200 470 275 400 L275 578 Z" fill="#123f96"/>
    <path d="M0 578 L0 550 C120 540 200 510 275 470 L275 578 Z" fill="#fff"/>
    <path d="M0 578 L0 530 C110 520 200 470 275 400 L275 420 C200 480 110 525 0 534 Z" fill="#fff" opacity="0"/>
  </svg>
  <svg class="svgfill" viewBox="0 0 275 578" aria-hidden="true">
    <path d="M0 548 C110 536 200 498 275 448 L275 578 L0 578 Z" fill="#123f96"/>
    <path d="M0 578 L0 560 C120 548 200 520 275 480 L275 578 Z" fill="#123f96"/>
  </svg>
  <div class="kicker abs" style="left:26px;top:100px">Wer wir sind</div>
  <h2 class="headline abs" style="left:26px;top:119px;font-size:24.5px">Vertrauen <span class="blue">beginnt</span><br><span class="serif">mit Zuhören.</span></h2>
  <div class="body abs" style="left:26px;top:178px;width:218px">
    <p>Pflege bedeutet für uns mehr als Versorgung. Es geht um Menschen, ihre Gewohnheiten, ihre Wünsche und das gute Gefühl, in den eigenen vier Wänden bleiben zu können.</p>
    <p style="margin-top:13px">Deshalb nehmen wir uns Zeit für persönliche Gespräche und individuelle Lösungen. Gemeinsam mit unseren Kundinnen, Kunden und Angehörigen gestalten wir eine Unterstützung, die zum Leben passt – nicht umgekehrt</p>
    <p style="margin-top:13px">Als ambulanter Pflegedienst begleiten wir Menschen im Raum Ilsede und Peine zuverlässig im Alltag und stehen auch Angehörigen beratend zur Seite.</p>
  </div>
  <svg class="quote-frame" style="left:26px;top:400px" width="220" height="56" viewBox="0 0 220 56" aria-hidden="true">
    <text x="0" y="14" font-family="Outfit,sans-serif" font-size="18" font-weight="700" fill="#123f96">”</text>
    <path d="M19 3 V13 M19 7.5 H185 Q200 7.5 200 22 V50" fill="none" stroke="#123f96" stroke-width="2"/>
  </svg>
  <p class="quote" style="left:26px;top:424px">Unsere Pflege orientiert sich<br>am Befinden der Menschen<br>– nicht am Befund.”</p>
</section>

<!-- Panel 3: Leistungen -->
<section class="panel p3" style="background:linear-gradient(180deg,var(--lighter) 0%,var(--light) 40%,#bdd3ef 100%)">
  <svg class="svgfill" viewBox="0 0 275 578" aria-hidden="true">
    <path d="M0 578 L0 545 C110 540 210 500 275 470 L275 578 Z" fill="#123f96"/>
    <path d="M0 578 L0 555 C120 548 210 520 275 490 L275 578 Z" fill="#123f96"/>
  </svg>
  <div class="kicker abs" style="left:26px;top:36px">Unsere Leistungen</div>
  <h2 class="headline abs" style="left:26px;top:63px;font-size:24.5px">Unterstützung, <span class="blue">die</span><br><span class="blue">den Alltag</span> <span class="serif">leichter</span><br><span class="serif blue">macht.</span></h2>
  <div class="services" style="top:158px">
    <div class="service" style="padding-bottom:14px"><div class="icon"><svg viewBox="0 0 20 20"><path d="M10 9 C7 6 5 8 7 10 L10 13 L13 10 C15 8 13 6 10 9Z M2 14 H6 L10 16 H15 L18 13"/></svg></div><div><h3>Grundpflege</h3><p>Unterstützung bei Körperpflege, Mobilität, Ernährung und allem, was Sicherheit im Alltag gibt.</p></div></div>
    <div class="service" style="padding-bottom:14px"><div class="icon"><svg viewBox="0 0 20 20"><path d="M10 2 V18 M5 6 H15 M7 10 C12 9 12 13 8 13"/></svg></div><div><h3>Behandlungspflege</h3><p>Medizinische Versorgung nach ärztlicher Verordnung – zum Beispiel Wundversorgung, Medikamentengabe oder Injektionen.</p></div></div>
    <div class="service" style="padding-bottom:14px"><div class="icon"><svg viewBox="0 0 20 20"><rect x="4" y="3" width="12" height="14" rx="1"/><path d="M10 8 V14 M7 11 H13"/></svg></div><div><h3>Betreuung &amp; Alltagsbegleitung</h3><p>Begleitung im Alltag, stundenweise Betreuung, Unterstützung bei Demenz sowie Entlastung für Angehörige.</p></div></div>
    <div class="service" style="padding-bottom:14px"><div class="icon"><svg viewBox="0 0 20 20"><circle cx="10" cy="6" r="3"/><path d="M4 18 C4 12 16 12 16 18"/></svg></div><div><h3>Verhinderungspflege</h3><p>Auszeiten im Rahmen der Verhinderungspflege, denn auch pflegende Angehörige müssen mal durchatmen.</p></div></div>
    <div class="service" style="padding-bottom:14px"><div class="icon"><svg viewBox="0 0 20 20"><circle cx="6" cy="8" r="2"/><circle cx="14" cy="8" r="2"/><path d="M3 17 V13 H9 V17 M11 17 V13 H17 V17 M8 3 H12"/></svg></div><div><h3>Beratung</h3><p>Pflegeberatung nach § 37.3 SGB XI zur Sicherstellung des Pflegegeld-Bezugs, Unterstützung bei Anträgen und Hilfe bei allen Fragen rund um Pflegeleistungen.</p></div></div>
  </div>
</section>

<!-- Panel 4: Leistungen 2 -->
<section class="panel p4" style="background:var(--light)">
  <div class="kicker abs" style="left:24px;top:45px">Unsere Leistungen</div>
  <div class="services" style="top:70px;left:17px;right:26px">
    <div class="service" style="padding:13px 0 13px 6px"><div class="icon"><svg viewBox="0 0 20 20"><path d="M10 15 L4 9 C2 6 6 2 10 6 C14 2 18 6 16 9 Z"/></svg></div><div><h3>Hausnotruf &amp; Erreichbarkeit</h3><p>Sicherheit rund um die Uhr – mit einem Team, das erreichbar bleibt.</p></div></div>
    <div class="service" style="padding:13px 0 13px 6px"><div class="icon"><svg viewBox="0 0 20 20"><circle cx="10" cy="6" r="3"/><path d="M5 18 V13 C5 10 15 10 15 13 V18 Z M10 12 V16 M8 14 H12"/></svg></div><div><h3>Palliative Versorgung</h3><p>Als spezialisierter Anbieter ist uns die Versorgung und Begleitung zum Ende des Lebens ein besonderes Herzensanliegen.</p></div></div>
  </div>
  <svg class="quote-frame" style="left:26px;top:226px" width="230" height="80" viewBox="0 0 230 80" aria-hidden="true">
    <text x="0" y="14" font-family="Outfit,sans-serif" font-size="18" font-weight="700" fill="#123f96">”</text>
    <path d="M19 3 V13 M19 7.5 H190 Q205 7.5 205 22 V75" fill="none" stroke="#123f96" stroke-width="2"/>
  </svg>
  <p class="quote" style="left:27px;top:245px">Unsere Pflege orientiert sich<br>am Befinden der Menschen<br>– nicht am Befund.”</p>
  <div class="photo" role="img" aria-label="Foto: Pflegeteam in Dienstkleidung am weißen Firmenwagen" style="left:0;top:330px;width:275px;height:248px;background:linear-gradient(160deg,#dfe4ea 0%,#b7c0cc 40%,#3d4f7c 70%,#6c7a63 100%)"></div>
  <svg class="svgfill" viewBox="0 0 275 578" aria-hidden="true">
    <path d="M0 541 C110 530 210 510 275 470 L275 578 L0 578 Z" fill="#123f96"/>
    <path d="M0 578 L0 573 C90 570 160 560 230 578 Z" fill="#123f96"/>
  </svg>
</section>

<!-- Panel 5: Was uns besonders macht -->
<section class="panel p5">
  <h2 class="headline abs" style="left:26px;top:40px;font-size:25px">Was uns<br><span class="blue">besonders</span> <span class="serif">macht.</span></h2>
  <h3 class="abs" style="left:26px;top:108px;font-size:12px;font-weight:400;line-height:1.15">Gute Pflege entsteht durch<br>Aufmerksamkeit, Erfahrung und ein<br>verlässliches Team.</h3>
  <p class="abs" style="left:26px;top:150px;width:215px;font-size:6.9px;font-weight:300;line-height:1.67;color:#333">Bei der Hauskrankenpflege Lindner arbeiten engagierte Pflegekräfte, Betreuungskräfte und Fachpersonen Hand in Hand – mit Herz, Respekt undfachlicher Kompetenz. Über 40 Mitarbeitende geben Tag für Tag ihr Bestes für Sie und Ihre Angehörigen.</p>
  <div class="dotted" style="top:207px"></div>
  <h3 class="abs" style="left:26px;top:218px;font-size:12px;font-weight:400">Wir sind für Sie da.</h3>
  <p class="abs" style="left:26px;top:241px;width:215px;font-size:6.9px;font-weight:300;line-height:1.67;color:#333">Sie möchten sich informieren oder ein persönliches Gespräch vereinbaren? Wir beraten Sie gerne – unkompliziert, persönlich und unverbindlich.</p>
  <div class="dotted" style="top:287px"></div>
  <p class="serif abs" style="left:26px;top:304px;font-size:10.5px;line-height:1.2">Hauskrankenpflege Lindner Ilseder<br>Am Anger 4 · 31241 Ilsede</p>
  <div class="contact abs" style="left:26px;top:340px">
    <div class="row"><svg viewBox="0 0 10 10"><path d="M2 1 L4 3 L3 4 C4 6 5 7 6 7 L7 6 L9 8 L8 9 C4 9 1 6 1 2 Z"/></svg>Telefon: 0 51 72 - 40 18 0</div>
    <div class="row"><svg viewBox="0 0 10 10"><rect x="1" y="2" width="8" height="6"/><path d="M1 2 L5 5 L9 2"/></svg>info@lindner-hauspflege.de</div>
    <div class="row"><svg viewBox="0 0 10 10"><circle cx="5" cy="5" r="4"/><path d="M1 5 H9 M5 1 C2 4 2 6 5 9 C8 6 8 4 5 1"/></svg>www.lindner-hauspflege.de</div>
  </div>
  <div class="contact abs" style="left:157px;top:340px">
    <div class="row"><svg viewBox="0 0 10 10"><path d="M5 9 C2 6 2 5 2 4 A3 3 0 0 1 8 4 C8 5 8 6 5 9Z"/></svg>Bürozeiten: Mo., Di., Mi.,</div>
    <div style="padding-left:7px">Fr. 9 bis 12 Uhr und Do.<br>15 bis 17 Uhr<br>Ergänzende Elemente</div>
  </div>
  <div class="photo" role="img" aria-label="Foto: Pflegekraft in Dienstjacke geht über eine Wiese zum Firmenwagen" style="left:0;top:400px;width:275px;height:178px;background:linear-gradient(180deg,#dfe6ef 0%,#c9d3dc 45%,#8b8a62 75%,#6b6a45 100%)"></div>
  <svg class="svgfill" viewBox="0 0 275 578" aria-hidden="true">
    <path d="M0 400 H275 V430 C200 400 140 410 90 425 L0 440 Z" fill="#fff"/>
    <path d="M100 422 C160 400 220 398 275 418 L275 428 C220 410 160 412 100 426 Z" fill="#123f96"/>
  </svg>
  <div class="badge" style="left:20px;top:385px;width:80px;height:62px;font-size:8.5px">Lindner<br>Hauspflege</div>
</section>

<!-- Panel 6: Haushaltsdienstleistungen -->
<section class="panel p6">
  <h2 class="headline abs" style="left:30px;top:30px;font-size:25px">Haushaltsdien<br>stleistungen</h2>
  <h3 class="abs" style="left:30px;top:84px;font-size:12px;font-weight:400">Haushaltshilfe. Entlastung im Alltag.</h3>
  <p class="abs" style="left:30px;top:108px;width:215px;font-size:6.9px;font-weight:300;line-height:1.67;color:#444">Damit Sie sich weiterhin zu Hause wohlfühlen, bietet Ihnen das Team von Lindner Hausdienste mit über 25 Kolleginnen und Kollegen professionelle und zuverlässige Unterstützung in verschiedenen Bereichen:</p>
  <div class="services" style="top:172px;left:22px;right:22px">
    <div class="service" style="border-top:none;padding:13px 0 10px 6px"><div class="icon" style="background:#e6e6e6"><svg viewBox="0 0 20 20" style="stroke:#333"><circle cx="6" cy="9" r="2"/><circle cx="14" cy="9" r="2"/><path d="M3 16 V13 H9 V16 M11 16 V13 H17 V16"/></svg></div><div><h3>Haushaltshilfe</h3><p>Unterstützung bei alltäglichen Aufgaben – von der gründlichen Reinigung bis zur Wäsche.</p></div></div>
    <div class="service" style="padding:11px 0 12px 6px"><div class="icon" style="background:#e6e6e6"><svg viewBox="0 0 20 20" style="stroke:#333"><circle cx="10" cy="5" r="2"/><path d="M4 8 L10 10 L16 8 M10 10 V14 M7 18 L10 14 L13 18"/></svg></div><div><h3>Begleitung</h3><p>Niemand ist gern allein, und wir sind für Sie da, wenn Sie Gesellschaft wünschen.</p></div></div>
    <div class="service" style="padding:11px 0 12px 6px"><div class="icon" style="background:#e6e6e6"><svg viewBox="0 0 20 20" style="stroke:#333"><path d="M10 9 C7 6 5 8 7 10 L10 13 L13 10 C15 8 13 6 10 9Z M2 14 H6 L10 16 H15 L18 13"/></svg></div><div><h3>Pflege</h3><p>Strukturierte Pflege und Unterstützung, individuell auf Ihre Bedürfnisse abgestimmt.</p></div></div>
  </div>
  <h3 class="abs" style="left:0;width:275px;text-align:center;top:345px;font-size:12px;font-weight:400">So erreichen Sie uns</h3>
  <p class="abs" style="left:25px;width:225px;text-align:center;top:365px;font-size:6.9px;font-weight:300;line-height:1.67;color:#444">Das Team von Lindner Home Services hilft Ihnen gerne bei Fragen und Terminwünschen weiter.</p>
  <svg class="svgfill" viewBox="0 0 275 578" aria-hidden="true">
    <path d="M0 578 V470 C40 440 90 448 137 452 C190 448 240 440 275 470 V578 Z" fill="#2b9a4f"/>
  </svg>
  <div class="photo" role="img" aria-label="Foto: lächelnde Mitarbeiterin in grüner Kleidung vor hellem Hintergrund" style="left:26px;top:397px;width:229px;height:98px;border:2px solid #fff;border-radius:0 0 8px 8px;background:linear-gradient(120deg,#cfdad6 0%,#b3c4bf 40%,#d8c1ad 62%,#3d7c57 100%)"></div>
  <p class="serif abs" style="left:0;width:275px;text-align:center;top:507px;font-size:10px;color:#eaf5ee">Lindner Home Services GmbH</p>
  <div class="contact abs" style="left:30px;top:530px;color:#fff;font-size:6.6px">
    <div class="row"><svg viewBox="0 0 10 10"><path d="M2 1 L4 3 L3 4 C4 6 5 7 6 7 L7 6 L9 8 L8 9 C4 9 1 6 1 2 Z"/></svg>Telefon: +49 51 72 - 55 20 140</div>
    <div class="row"><svg viewBox="0 0 10 10"><rect x="1" y="2" width="8" height="6"/><path d="M1 2 L5 5 L9 2"/></svg>info@lindner-hausdienste.de</div>
    <div class="row"><svg viewBox="0 0 10 10"><circle cx="5" cy="5" r="4"/><path d="M1 5 H9 M5 1 C2 4 2 6 5 9 C8 6 8 4 5 1"/></svg>www.lindner-hausdienste.de</div>
  </div>
  <div class="contact abs" style="left:155px;top:530px;color:#fff;font-size:6.6px">
    <div class="row"><svg viewBox="0 0 10 10"><path d="M5 9 C2 6 2 5 2 4 A3 3 0 0 1 8 4 C8 5 8 6 5 9Z"/></svg>Bürozeiten: Mo., Di., Mi., Fr. 9 bis</div>
    <div style="padding-left:7px">12 Uhr und Do. 15 bis 17 Uhr<br>Ergänzende Elemente</div>
  </div>
</section>

</body>
</html>
```